Health software company called BRIGHT MERIDIAN, committed to innovation and technological excellence

The powerpoint presentation template is necessary, very necessary is elegant and modern with innovative images and the color palette attached. The presentation will be used for the business plan and investor presentations that we will use to raise funds. Please, recommend a modern typeface, as well as format to be able to use it and incorporate it as part of the company's brand guidelines. Great diversity of technological solutions
Updates

Very low attendance of designers for a high budget. Very few proposals and no capture my interest

Need extra days to review

Need extra days to review

Need extra days to review

Target Market(s)

managers, managers of public and private health centers, government states, investors

Industry/Entity Type

It Company

Font styles to use
Serif

Requirements
Must have
• The powerpoint presentation template is necessary, very necessary is elegant, minimalist and modern with innovative images and the color palette attached. it must be refined in demarcated style
Nice to have
• very nice, visually harmonic avoid saturation
Should not have
• NO dark colors NO dark colors NO dark colors NO dark colors NO dark colors

```html
<!DOCTYPE html>
<html lang="en">
<head>
<meta charset="utf-8">
<title>Bright Meridian — Presentation Template</title>
<link rel="stylesheet" href="https://fonts.googleapis.com/css2?family=Montserrat:wght@400;500;600;700&display=swap">
<style>
  :root{
    --canvas:#efefef;
    --paper:#ffffff;
    --mist:#e8f0f3;
    --mist-deep:#d7e4ea;
    --ink:#2b2f33;
    --teal:#6ccadf;
    --sky:#1a93c2;
    --blue:#4a7fc1;
    --line:#6b7378;
    --corner:#c3d3da;
  }
  *{box-sizing:border-box;margin:0;padding:0}
  html,body{width:1200px;height:1200px;overflow:hidden}
  body{background:var(--canvas);font-family:"Montserrat",sans-serif;color:var(--ink);position:relative}
  .slide{position:absolute;width:571px;height:321px;overflow:hidden;background:var(--paper);box-shadow:0 0 0 1px #e0e0e0}
  .slide--tint{background:var(--mist)}
  .col-left{left:20px}.col-right{left:606px}
  .row-1{top:78px}.row-2{top:438px}.row-3{top:806px}
  .abs{position:absolute}
  .photo{position:absolute}
  .footer{position:absolute;left:34px;right:32px;top:300px;display:flex;align-items:center;gap:6px;font-size:8.5px;font-weight:500;color:var(--ink)}
  .footer .rule{flex:1;height:1px;background:var(--line)}
  .footer .page{font-weight:700;font-size:7px;width:10px;text-align:right}
  .accent-bar{position:absolute;height:3px;background:var(--blue)}
  .lead{color:var(--blue);font-weight:600;font-size:7.8px;line-height:1.35;letter-spacing:.2px;text-align:justify}
  .body{font-size:6.9px;line-height:1.33;text-align:justify;letter-spacing:-.15px;color:var(--ink)}
  .corner{position:absolute;left:0;top:0}

  /* slide 2 */
  .hero-photo{inset:0;background:linear-gradient(160deg,#f4f7f8 0%,#dfe7eb 50%,#c9d5db 100%)}
  .hero-text{position:absolute;left:30px;top:206px;color:var(--ink)}
  .hero-text .bar{width:30px;height:3px;background:var(--teal);margin-bottom:8px}
  .hero-text .kicker{font-size:12px;font-weight:500;letter-spacing:.3px}
  .hero-text .title{font-size:18.5px;font-weight:700;line-height:1.25;letter-spacing:.6px}
  .hero-text .title .hl{color:var(--sky)}

  /* slide 3 */
  .feature{position:absolute;left:314px;width:190px}
  .feature .icon-box{position:absolute;left:0;top:-4px;width:34px;height:34px;border:1px solid var(--ink);display:flex;align-items:center;justify-content:center;background:var(--paper)}
  .feature .name{position:absolute;left:44px;top:0;color:var(--sky);font-weight:700;font-size:10.5px;letter-spacing:.3px}
  .feature .body{position:absolute;left:44px;top:14px;width:140px;text-align:left}

  /* slide 4 */
  .panel{position:absolute;left:32px;top:54px;width:173px;height:212px;background:var(--teal);display:flex;align-items:center;justify-content:center}
  .statement{position:absolute;left:236px;top:113px;width:301px;color:var(--ink)}
  .statement .kicker{font-size:12px;font-weight:500}
  .statement .title{font-size:18px;font-weight:700;line-height:1.05;letter-spacing:.2px}
  .statement .rule{height:2px;background:var(--teal);margin:5px 0 6px}

  /* slide 5 */
  .section-title{position:absolute;font-size:20.5px;font-weight:700;letter-spacing:.6px;color:var(--ink)}
  .section-rule{position:absolute;height:1px;background:var(--ink)}

  /* slide 6 */
  .band{position:absolute;left:0;right:0;top:120px;bottom:0;background:var(--mist)}
  .service{position:absolute;top:90px;width:140px;margin-left:-70px;text-align:center}
  .service .circle{width:60px;height:60px;border-radius:50%;background:var(--teal);margin:0 auto;display:flex;align-items:center;justify-content:center}
  .service .name{margin-top:11px;color:var(--sky);font-weight:700;font-size:10.5px;letter-spacing:.3px}
  .service .body{margin-top:4px;text-align:justify;text-align-last:center}
</style>
</head>
<body>

<!-- Slide 1 -->
<section class="slide col-left row-1">
  <svg class="corner" width="122" height="122" viewBox="0 0 122 122"><polygon points="0,0 122,0 0,122" fill="var(--corner)"/></svg>
  <div class="photo" role="img" aria-label="Photo of two colleagues at a computer screen, one pointing with a pen" style="left:30px;top:26px;width:370px;height:269px;background:linear-gradient(120deg,#9aa3a8 0%,#cfd6d9 45%,#f1f3f4 100%)"></div>
  <div class="accent-bar" style="left:413px;top:101px;width:42px"></div>
  <p class="lead abs" style="left:413px;top:108px;width:128px">Lorem Ipsum is simply dummy text of the printing and typesetting industry.</p>
  <p class="body abs" style="left:413px;top:152px;width:140px">Lorem Ipsum is simply dummy text of the printing and typesetting industry. Lorem Ipsum has been the industry's standard dummy text ever since the 1500s, when an unknown printer took a galley of type and scrambled it to make a type specimen book.</p>
  <div class="footer"><span>www.website.com</span><span class="rule"></span><span class="page">1.</span></div>
</section>

<!-- Slide 2 -->
<section class="slide col-right row-1">
  <div class="photo hero-photo" role="img" aria-label="Soft photo of a keyboard, phone and pen on a desk"></div>
  <div class="hero-text">
    <div class="bar"></div>
    <div class="kicker">WE GROW OUT</div>
    <div class="title"><span class="hl">BUSINESS BEYOUNG</span><br>POSSIBLE LIMITS</div>
  </div>
  <div class="footer"><span>www.website.com</span><span class="rule"></span><span class="page">2.</span></div>
</section>

<!-- Slide 3 -->
<section class="slide slide--tint col-left row-2">
  <div class="photo" role="img" aria-label="Photo of a team gathered around a laptop" style="left:0;top:33px;width:286px;height:246px;background:linear-gradient(150deg,#e4e8ea 0%,#aab3b8 55%,#eef1f2 100%)"></div>
  <div class="feature" style="top:37px">
    <div class="icon-box"><svg width="24" height="24" viewBox="0 0 24 24"><circle cx="9" cy="9" r="6" fill="none" stroke="var(--ink)" stroke-width="2"/><circle cx="9" cy="9" r="3" fill="var(--teal)"/><line x1="13.5" y1="13.5" x2="21" y2="21" stroke="var(--ink)" stroke-width="3" stroke-linecap="round"/></svg></div>
    <div class="name">LOREM IPSUM</div>
    <p class="body">Lorem Ipsum is simply dummy text of the printing and typesetting industry. Lorem Ipsum has been the industry's standard dummy text.</p>
  </div>
  <div class="feature" style="top:106px">
    <div class="icon-box"><svg width="24" height="24" viewBox="0 0 24 24"><circle cx="9" cy="9" r="6" fill="none" stroke="var(--ink)" stroke-width="2"/><circle cx="9" cy="9" r="3" fill="var(--teal)"/><line x1="13.5" y1="13.5" x2="21" y2="21" stroke="var(--ink)" stroke-width="3" stroke-linecap="round"/></svg></div>
    <div class="name">LOREM IPSUM</div>
    <p class="body">Lorem Ipsum is simply dummy text of the printing and typesetting industry. Lorem Ipsum has been the industry's standard dummy text.</p>
  </div>
  <div class="feature" style="top:171px">
    <div class="icon-box"><svg width="24" height="24" viewBox="0 0 24 24"><circle cx="9" cy="9" r="6" fill="none" stroke="var(--ink)" stroke-width="2"/><circle cx="9" cy="9" r="3" fill="var(--teal)"/><line x1="13.5" y1="13.5" x2="21" y2="21" stroke="var(--ink)" stroke-width="3" stroke-linecap="round"/></svg></div>
    <div class="name">LOREM IPSUM</div>
    <p class="body">Lorem Ipsum is simply dummy text of the printing and typesetting industry. Lorem Ipsum has been the industry's standard dummy text.</p>
  </div>
  <div class="feature" style="top:236px">
    <div class="icon-box"><svg width="24" height="24" viewBox="0 0 24 24"><circle cx="9" cy="9" r="6" fill="none" stroke="var(--ink)" stroke-width="2"/><circle cx="9" cy="9" r="3" fill="var(--teal)"/><line x1="13.5" y1="13.5" x2="21" y2="21" stroke="var(--ink)" stroke-width="3" stroke-linecap="round"/></svg></div>
    <div class="name">LOREM IPSUM</div>
    <p class="body">Lorem Ipsum is simply dummy text of the printing and typesetting industry. Lorem Ipsum has been the industry's standard dummy text.</p>
  </div>
  <div class="footer"><span>www.website.com</span><span class="rule"></span><span class="page">3.</span></div>
</section>

<!-- Slide 4 -->
<section class="slide slide--tint col-right row-2">
  <div class="panel">
    <svg width="84" height="92" viewBox="0 0 84 92">
      <path d="M52 78 H6 V10 H70 V56" fill="none" stroke="var(--ink)" stroke-width="5" stroke-linejoin="round"/>
      <rect x="28" y="2" width="20" height="12" rx="3" fill="var(--ink)"/>
      <rect x="20" y="10" width="36" height="6" fill="var(--ink)"/>
      <g stroke="var(--ink)" stroke-width="3.5">
        <line x1="16" y1="28" x2="58" y2="28"/><line x1="16" y1="36" x2="58" y2="36"/>
        <line x1="16" y1="44" x2="58" y2="44"/><line x1="16" y1="52" x2="58" y2="52"/>
        <line x1="16" y1="60" x2="50" y2="60"/>
      </g>
      <polyline points="48,70 60,82 82,60" fill="none" stroke="var(--ink)" stroke-width="6" stroke-linecap="round" stroke-linejoin="round"/>
    </svg>
  </div>
  <div class="statement">
    <div class="kicker">We grow out</div>
    <div class="title">Business beyoung<br>Possible limits</div>
    <div class="rule"></div>
    <p class="body">Lorem Ipsum is simply dummy text of the printing and typesetting industry. Lorem Ipsum has been the industry's standard dummy text. Lorem Ipsum is simply dummy text of the printing and typesetting industry. Lorem Ipsum has been the industry's standard dummy text.</p>
  </div>
  <div class="footer"><span>www.website.com</span><span class="rule"></span><span class="page">4.</span></div>
</section>

<!-- Slide 5 -->
<section class="slide col-left row-3">
  <div class="photo" role="img" aria-label="Photo of a businessman looking out of a window over a city" style="left:33px;top:60px;width:173px;height:211px;background:linear-gradient(180deg,#c2cbd0 0%,#a3aeb4 55%,#7f8a90 100%)"></div>
  <h2 class="section-title" style="left:227px;top:68px">COMPANY CONTENT</h2>
  <div class="section-rule" style="left:227px;top:93px;width:305px"></div>
  <div class="accent-bar" style="left:227px;top:117px;width:40px"></div>
  <p class="lead abs" style="left:227px;top:123px;width:277px">Lorem Ipsum is simply dummy text of the printing and typesetting industry.</p>
  <p class="body abs" style="left:227px;top:163px;width:310px">Lorem ipsum dolor sit amet, consectetur adipiscing elit, sed do eiusmod tempor incididunt ut labore et dolore magna aliqua. Ut enim ad minim veniam, quis nostrud exercitation ullamco laboris nisi ut aliquip ex ea commodo consequat. Duis aute irure dolor in reprehenderit in voluptate velit esse cillum dolore eu fugiat nulla pariatur. Excepteur sint occaecat cupidatat non proident, sunt in culpa qui officia deserunt mollit anim id est laborum.</p>
  <div class="footer"><span>www.website.com</span><span class="rule"></span><span class="page">5.</span></div>
</section>

<!-- Slide 6 -->
<section class="slide col-right row-3">
  <div class="band"></div>
  <h2 class="section-title" style="left:34px;top:28px">OUR SERVICES</h2>
  <div class="section-rule" style="left:32px;top:54px;width:305px"></div>
  <div class="service" style="left:107px">
    <div class="circle"><svg width="30" height="30" viewBox="0 0 24 24"><circle cx="9" cy="9" r="6" fill="none" stroke="var(--ink)" stroke-width="2"/><circle cx="9" cy="9" r="3" fill="#fff"/><line x1="13.5" y1="13.5" x2="21" y2="21" stroke="var(--ink)" stroke-width="3" stroke-linecap="round"/></svg></div>
    <div class="name">LOREM IPSUM</div>
    <p class="body">Lorem Ipsum is simply dummy text of the printing and typesetting industry. Lorem Ipsum has been the industry's standard dummy text. Lorem Ipsum is simply dummy text of the printing and typesetting industry. Lorem Ipsum has been the industry's standard dummy text.</p>
  </div>
  <div class="service" style="left:286px">
    <div class="circle"><svg width="30" height="30" viewBox="0 0 24 24"><circle cx="9" cy="9" r="6" fill="none" stroke="var(--ink)" stroke-width="2"/><circle cx="9" cy="9" r="3" fill="#fff"/><line x1="13.5" y1="13.5" x2="21" y2="21" stroke="var(--ink)" stroke-width="3" stroke-linecap="round"/></svg></div>
    <div class="name">LOREM IPSUM</div>
    <p class="body">Lorem Ipsum is simply dummy text of the printing and typesetting industry. Lorem Ipsum has been the industry's standard dummy text. Lorem Ipsum is simply dummy text of the printing and typesetting industry. Lorem Ipsum has been the industry's standard dummy text.</p>
  </div>
  <div class="service" style="left:463px">
    <div class="circle"><svg width="30" height="30" viewBox="0 0 24 24"><circle cx="9" cy="9" r="6" fill="none" stroke="var(--ink)" stroke-width="2"/><circle cx="9" cy="9" r="3" fill="#fff"/><line x1="13.5" y1="13.5" x2="21" y2="21" stroke="var(--ink)" stroke-width="3" stroke-linecap="round"/></svg></div>
    <div class="name">LOREM IPSUM</div>
    <p class="body">Lorem Ipsum is simply dummy text of the printing and typesetting industry. Lorem Ipsum has been the industry's standard dummy text. Lorem Ipsum is simply dummy text of the printing and typesetting industry. Lorem Ipsum has been the industry's standard dummy text.</p>
  </div>
  <div class="footer"><span>www.website.com</span><span class="rule"></span><span class="page">6.</span></div>
</section>

</body>
</html>
```